Bright Path Safety billboard design project.

Bright Path Safety Ltd. is based in Quesnel BC and provides a variety of safety services including COR external auditing, safety training, over 500 online safety courses, mobile equipment training and heavy duty equipment training. We are looking for a billboard design with more of a focus on the mobile equipment training.

Target Market(s)

Construction, forestry and mining companies.

Colors
3276b5

Requirements
Must have
• Company Logo
website www.brightpathsafety-example.com

```html
<!DOCTYPE html>
<html lang="en">
<head>
<meta charset="utf-8">
<title>Bright Path Safety – Mobile Equipment Billboard</title>
<link rel="stylesheet" href="https://fonts.googleapis.com/css2?family=Archivo+Black&family=Montserrat:wght@400;700;800&display=swap">
<style>
  :root {
    --brand-blue: #3276b5;
    --page-bg: #e9ecef;
    --text-white: #ffffff;
    --photo-light: #8a94a6;
    --photo-dark: #4b5466;
  }
  * { box-sizing: border-box; margin: 0; padding: 0; }
  html, body {
    width: 1200px;
    height: 962px;
    overflow: hidden;
    background: var(--page-bg);
  }
  .billboard {
    position: absolute;
    left: 40px;
    top: 351px;
    width: 1120px;
    height: 260px;
    background: var(--brand-blue);
    color: var(--text-white);
    overflow: hidden;
  }
  .team-photo {
    position: absolute;
    left: 363px;
    top: 8px;
    width: 205px;
    height: 252px;
    background: linear-gradient(180deg, var(--photo-light), var(--photo-dark));
    border-radius: 6px 6px 0 0;
  }
  .tagline-left {
    position: absolute;
    left: 65px;
    top: 168px;
    font-family: "Montserrat", sans-serif;
    font-weight: 800;
    font-size: 25px;
    letter-spacing: 0.3px;
    white-space: nowrap;
  }
  .headline {
    position: absolute;
    left: 615px;
    top: 26px;
    font-family: "Archivo Black", sans-serif;
    font-weight: 400;
    font-size: 42px;
    line-height: 50px;
    letter-spacing: 1px;
    white-space: nowrap;
  }
  .brand-block {
    position: absolute;
    left: 621px;
    top: 150px;
    width: 480px;
    height: 90px;
  }
  .brand-mark {
    position: absolute;
    left: 0;
    top: 6px;
    width: 44px;
    height: 44px;
    border-radius: 50%;
    background: var(--text-white);
  }
  .brand-name {
    position: absolute;
    left: 56px;
    top: 14px;
    font-family: "Montserrat", sans-serif;
    font-weight: 700;
    font-size: 19px;
    white-space: nowrap;
  }
  .website {
    position: absolute;
    left: 56px;
    top: 46px;
    font-family: "Montserrat", sans-serif;
    font-weight: 800;
    font-size: 16px;
    white-space: nowrap;
  }
  .motto {
    position: absolute;
    left: 56px;
    top: 68px;
    font-family: "Montserrat", sans-serif;
    font-weight: 400;
    font-size: 13px;
    white-space: nowrap;
  }
</style>
</head>
<body>
  <section class="billboard">
    <div class="team-photo" role="img" aria-label="Photo of a worker in a hard hat and overalls talking with a manager holding a tablet"></div>
    <p class="tagline-left">Specialized Professionals</p>
    <h1 class="headline">Mobile Equipment<br>Training &amp; Safety</h1>
    <div class="brand-block">
      <span class="brand-mark"></span>
      <span class="brand-name">Bright Path Safety Ltd.</span>
      <span class="website">www.brightpathsafety-example.com</span>
      <span class="motto">Together as a team we work safely, every day</span>
    </div>
  </section>
</body>
</html>
```